AI Layout work for Business Cards, Letterhead and Compliment Slip for Award-winning UK Property Deve

No actual logo or corporate identity design work needed here but some skill required to create layouts for business card, letterhead and compliment slip for this award-winning company.
I can provide AI files featuring the company logo and an initial layout of the business card, (6 versions featuring the same design but for different personnel), along with some initial instructions (with possibly more to follow from the client). The finished layouts for each item need to be print-ready in AI format - 8 in all (6 for each business card plus 1 for letterhead and 1 for compliment slip).
I've given this project a 5-day duration but there may be some flexibility built into that depending on client feedback. Hopefully that won't be a problem.
UPDATE:
The client has been very prescriptive about the layout and design of these. To that end, please find 3 additional pdfs that explain what's required.
1.
All BUSINESS CARDS need to be laid out as per the attached AI file (but see latest pdf to check which layout - there are 2 in the original AI file). Use the details in the RUNE-contact-details.pdf to create 6 individual AI files, one for each card.
2.
Create 2 additional AI files, one each for the LETTERHEAD and the COMPLIMENT SLIP based on the latest mock-up that I've provided (letterhead-layout-final.pdf)
In all, I need EIGHT individual AI files, 6 for each business card, 1 for the letterhead and 1 for the compliment slip. I'd like to get this done as soon as possible now please.
Target Market(s)
Purchasers of upmarket luxury properties - see here: http://www.runeestates.co.uk
Industry/Entity Type
Business
Requirements
Must have
- Layouts need to be cool, understated and uncluttered.
Nice to have
- Please keep it simple! The actual logo background colour is likely to change (awaiting confirmation from client) but accompanying text detail and font (Deja Vu Sans Condensed) can remain as seen in the files below - for the time being at least! That having been said, I'm open to suggestions.
Should not have
- Nothing extreme or ostentatious please.

```html
<!DOCTYPE html>
<html lang="en">
<head>
<meta charset="utf-8">
<title>RUNE – Business Card</title>
<link rel="stylesheet" href="https://fonts.googleapis.com/css2?family=PT+Sans:wght@400;700&display=swap">
<style>
  :root {
    --backdrop: #d6d6d6;
    --card: #f7f7f5;
    --navy: #1f2a5c;
    --ink: #1a1a1a;
    --ink-soft: #333333;
    --white: #ffffff;
    --card-w: 680px;
    --card-h: 440px;
  }
  * { box-sizing: border-box; margin: 0; padding: 0; }
  html, body {
    width: 1200px; height: 1200px; overflow: hidden;
    background: var(--backdrop);
    font-family: "PT Sans", sans-serif;
  }
  .sheet {
    width: 1200px; height: 1200px;
    display: flex; flex-direction: column;
    align-items: center; justify-content: center; gap: 70px;
  }
  .card {
    position: relative;
    width: var(--card-w); height: var(--card-h);
    background: var(--card);
    box-shadow: 0 2px 6px rgba(0,0,0,0.12);
  }

  /* Contact side */
  .person { position: absolute; left: 88px; top: 44px; color: var(--ink); }
  .person-name { font-size: 36px; font-weight: 700; line-height: 1; }
  .person-role { font-size: 20px; color: var(--ink-soft); margin-top: 4px; }

  .contact-lines {
    position: absolute; left: 402px; top: 124px;
    list-style: none; font-size: 16px; line-height: 1.35; color: var(--ink-soft);
  }

  .brand-block {
    position: absolute; left: 0; top: 188px;
    width: 250px; height: 112px;
    background: var(--navy); color: var(--white);
    display: flex; align-items: center; justify-content: center;
  }
  .brand-block .brand-name { font-size: 44px; font-weight: 400; line-height: 1; letter-spacing: 1px; }

  .address {
    position: absolute; left: 268px; top: 196px;
    font-style: normal; font-size: 19px; line-height: 1.2; color: var(--ink);
  }

  /* Brand side */
  .card-front {
    display: flex; align-items: center; justify-content: center;
    color: var(--navy);
  }
  .card-front .brand-name { font-size: 104px; font-weight: 400; line-height: 1; letter-spacing: 2px; }
</style>
</head>
<body>
  <main class="sheet">
    <section class="card card-back" aria-label="Business card, contact side">
      <div class="person">
        <p class="person-name">Daniel Hartley</p>
        <p class="person-role">Director</p>
      </div>
      <ul class="contact-lines">
        <li>+44 (0)1632 960418</li>
        <li>enquiries@runeestates.co.uk</li>
        <li>runeestates.co.uk</li>
      </ul>
      <div class="brand-block">
        <span class="brand-name">RUNE</span>
      </div>
      <address class="address">
        RUNE Exclusive Properties<br>
        Ashcombe House<br>
        Ashcombe Lane<br>
        Little Haddon<br>
        HP9 2QX
      </address>
    </section>

    <section class="card card-front" aria-label="Business card, brand side">
      <span class="brand-name">RUNE</span>
    </section>
  </main>
</body>
</html>
```